Varnelux7 website

Need to create a website for my business

Target Market(s)

Food ingredient companies, B2B

Industry/Entity Type

Food technology, food ingredients

Coding

Number of Pages Required

2 page

Requirements
Nice to have
• Case studies, links to articles,

```html
<!DOCTYPE html>
<html lang="en">
<head>
<meta charset="utf-8">
<title>Varnelux7 — Food Ingredient Technology</title>
<link rel="stylesheet" href="https://fonts.googleapis.com/css2?family=Ubuntu:wght@500;700&family=Montserrat:wght@300;400;500;600;700;800&display=swap">
<style>
:root{
  --green:#1f8a2c;
  --green-dark:#147020;
  --green-light:#7cc242;
  --ink:#222;
  --muted:#666;
  --panel:#f4f4f4;
  --grey:#ececec;
  --black:#000;
  --white:#fff;
}
*{box-sizing:border-box;margin:0;padding:0}
html,body{width:1200px;height:4070px;overflow:hidden}
body{position:relative;font-family:"Montserrat",sans-serif;color:var(--ink);background:var(--white)}
.abs{position:absolute}
.heading{font-family:"Ubuntu",sans-serif;font-weight:700}
.btn{position:absolute;display:flex;align-items:center;justify-content:space-between;padding:0 10px 0 18px;font-weight:600;font-size:12px;letter-spacing:.3px;border-radius:3px}
.btn-green{background:var(--green);color:var(--white);box-shadow:0 2px 4px rgba(0,0,0,.2)}
.btn-white{background:var(--white);color:var(--green)}
.btn .arrow{width:24px;height:24px;border-radius:50%;display:flex;align-items:center;justify-content:center}
.btn-green .arrow{background:var(--white)}
.btn-white .arrow{border:1px solid #bbb}
.brand{font-family:"Montserrat",sans-serif;font-weight:400;letter-spacing:4px;text-transform:uppercase;white-space:nowrap}
.brand-dot{position:absolute;border-radius:50%;background:var(--green)}

/* header */
.topbar{left:0;top:0;width:1200px;height:76px;background:var(--white);border-top:3px solid var(--green)}
.contact-item{font-size:13px;display:flex;align-items:center;gap:10px;top:28px;white-space:nowrap}
.social{width:32px;height:32px;border-radius:50%;border:1.5px solid var(--green);top:24px}

/* hero */
.hero{left:0;top:76px;width:1200px;height:641px;background:linear-gradient(180deg,#4a5158 0%,#6e6a63 45%,#a4643a 75%,#c0552a 100%)}
.nav{top:96px;left:0;width:1200px;font-size:14px;font-weight:600;color:var(--white)}
.nav span{position:absolute;top:0;white-space:nowrap}
.nav .active{color:#6fc24a;border-bottom:2px solid #6fc24a;padding-bottom:6px}
.hero-title{left:110px;top:270px;font-size:68px;color:var(--white);letter-spacing:-1px;font-family:"Montserrat",sans-serif;font-weight:800;white-space:nowrap}
.hero-sub{left:112px;top:356px;font-size:22px;line-height:31px;font-weight:600;color:var(--white);white-space:nowrap}
.slide-arrow{width:58px;height:58px;border-radius:50%;border:2px solid rgba(255,255,255,.8);top:348px;display:flex;align-items:center;justify-content:center}
.dot{width:11px;height:11px;border-radius:50%;border:1.5px solid var(--white);top:678px}

/* focus */
.focus{left:0;top:717px;width:1200px;height:504px;background:var(--panel)}
.focus-title{left:617px;top:778px;font-size:42px;color:#2e2e2e;font-weight:500;white-space:nowrap}
.focus-sub{left:617px;top:835px;width:480px;font-family:"Ubuntu",sans-serif;font-size:20px;line-height:31px;font-weight:500;color:#333}
.body-copy{font-size:14.5px;line-height:25.6px;color:#777}

/* services */
.services{left:0;top:1221px;width:1200px;height:829px;background:linear-gradient(180deg,#dedede 0%,#f3f3f3 55%,#fafafa 100%)}
.center-text{left:0;width:1200px;text-align:center}
.svc-label{font-size:15px;font-weight:600;color:#333;white-space:nowrap}

/* sustainable */
.sustain{left:0;top:2050px;width:1200px;height:492px;background:var(--green)}

/* articles */
.card{top:2676px;width:310px;height:403px;background:var(--white);box-shadow:0 1px 6px rgba(0,0,0,.18)}
.card .photo{position:absolute;left:8px;top:8px;width:294px;height:202px}
.card .meta{position:absolute;left:15px;top:228px;font-size:12.5px;color:var(--green);font-weight:500;white-space:nowrap}
.card .title{position:absolute;left:15px;top:256px;width:292px;font-size:17.5px;line-height:28px;font-weight:600;color:#1a1a1a;white-space:nowrap;letter-spacing:-.2px}
.card .text{position:absolute;left:17px;top:318px;width:282px;font-size:12px;line-height:20px;color:#777}
.card .link{position:absolute;left:15px;top:372px;font-size:13.5px;font-weight:600;color:var(--green);text-decoration:underline;display:flex;align-items:center;gap:10px;white-space:nowrap}

/* contact */
.contact{left:0;top:3169px;width:1200px;height:490px;background:var(--grey)}
.field-label{font-size:12px;color:#444;font-weight:500}
.field{background:#dcdcdc;font-size:11px;color:#888;padding:0 9px;display:flex;align-items:center}

/* footer */
.footer{left:0;top:3659px;width:1200px;height:411px;background:var(--black);color:var(--white)}
.foot-head{font-family:"Ubuntu",sans-serif;font-weight:700;font-size:21px;top:3720px;color:var(--white);white-space:nowrap}
.foot-head::after{content:"";display:block;width:40px;height:2px;background:var(--green);margin-top:10px}
.foot-list{top:3776px;font-size:13.5px;line-height:25.7px;list-style:none;color:var(--white);white-space:nowrap}
.foot-small{font-size:10px;color:#bbb}
.foot-text{font-size:13.5px;color:var(--white);white-space:nowrap}
.foot-legal{font-size:11.5px;font-weight:500;color:var(--white);white-space:nowrap}
</style>
</head>
<body>

<!-- Header -->
<header class="abs topbar">
  <div class="brand-dot" style="left:112px;top:14px;width:34px;height:34px"></div>
  <div class="abs brand" style="left:172px;top:15px;font-size:25px;color:#333">Varnelux7</div>
  <div class="abs" style="left:176px;top:52px;font-size:15px;color:#333;white-space:nowrap">Results Matter. Work Hard.</div>

  <div class="abs contact-item" style="left:529px">
    <svg width="20" height="20" viewBox="0 0 24 24"><path d="M6.6 10.8c1.4 2.8 3.8 5.1 6.6 6.6l2.2-2.2c.3-.3.7-.4 1-.2 1.1.4 2.3.6 3.6.6.6 0 1 .4 1 1V20c0 .6-.4 1-1 1C10.6 21 3 13.4 3 4c0-.6.4-1 1-1h3.5c.6 0 1 .4 1 1 0 1.3.2 2.5.6 3.6.1.3 0 .7-.2 1z" fill="var(--green)"/></svg>
    +1 (555) 010 4420
  </div>
  <div class="abs contact-item" style="left:723px">
    <svg width="22" height="16" viewBox="0 0 22 16"><rect x="1" y="1" width="20" height="14" fill="var(--green)"/><path d="M1 1l10 8 10-8" stroke="#fff" stroke-width="1.6" fill="none"/></svg>
    hello@varnelux7-mail.com
  </div>
  <div class="abs" style="left:945px;top:24px;width:1px;height:30px;background:#ccc"></div>
  <div class="abs social" style="left:968px"></div>
  <div class="abs social" style="left:1010px"></div>
  <div class="abs social" style="left:1053px"></div>
</header>

<!-- Hero -->
<section class="abs hero" role="img" aria-label="Food technologist in hairnet and lab coat inspecting an apple with a tablet beside a fruit sorting conveyor"></section>
<nav class="abs nav">
  <span class="active" style="left:484px">Home</span>
  <span style="left:566px">About Us</span>
  <span style="left:671px">Our Services</span>
  <span style="left:797px">Case Study</span>
  <span style="left:915px">Our Blog</span>
  <span style="left:1016px">Contact Us</span>
</nav>
<h1 class="abs hero-title">VARNELUX7</h1>
<p class="abs hero-sub">Perspiciatis unde omniste natuserors<br>Isdroit voluptatem accusantium.</p>
<div class="btn btn-green" style="left:112px;top:442px;width:215px;height:44px;font-size:15px;background:#1e9a2a">GET STARTED
  <span class="arrow" style="width:28px;height:28px"><svg width="14" height="12" viewBox="0 0 14 12"><path d="M1 6h11M7 1l5 5-5 5" stroke="#1e9a2a" stroke-width="2" fill="none"/></svg></span>
</div>
<div class="abs slide-arrow" style="left:25px"><svg width="20" height="14" viewBox="0 0 20 14"><path d="M19 7H2M8 1L2 7l6 6" stroke="#fff" stroke-width="2" fill="none"/></svg></div>
<div class="abs slide-arrow" style="left:1117px"><svg width="20" height="14" viewBox="0 0 20 14"><path d="M1 7h17M12 1l6 6-6 6" stroke="#fff" stroke-width="2" fill="none"/></svg></div>
<div class="abs dot" style="left:564px"></div>
<div class="abs dot" style="left:584px;background:var(--green);border-color:var(--green)"></div>
<div class="abs dot" style="left:604px"></div>
<div class="abs dot" style="left:623px"></div>

<!-- Areas of focus -->
<section class="abs focus">
  <svg class="abs" style="left:0;top:0" width="460" height="504">
    <polygon points="0,0 379,0 458,504 0,504" fill="#2f8c31"/>
  </svg>
  <div class="abs" role="img" aria-label="Green leafy crops growing in a greenhouse with a worker holding a tablet" style="left:0;top:0;width:400px;height:504px;background:linear-gradient(120deg,rgba(40,120,40,.0),rgba(30,110,30,.35))"></div>
  <div class="abs" style="left:584px;top:76px;width:8px;height:335px;background:var(--green)"></div>
  <div class="abs" role="img" aria-label="Hands holding a tablet inside a greenhouse above rows of lettuce" style="left:167px;top:68px;width:417px;height:342px;background:linear-gradient(180deg,#dfe8e6 0%,#a9c6a1 40%,#5f9a3c 75%,#3d7a25 100%)"></div>
</section>
<h2 class="abs heading focus-title">Areas of focus</h2>
<p class="abs focus-sub">Fermentation-derived ingredients that improve<br>supply chains.</p>
<p class="abs body-copy" style="left:616px;top:908px;width:460px">Perspiciatis unde omnis iste natus error sit voluptatem accusantium doloremque laudantium, totam rem aperiam, eaque ipsa quae ab illo inventore veritatis et quasi architecto beatae vitae dicta sunt explicabo. Nemo enim ipsam voluptatem quia voluptas sit aspernatur aut odit aut fugit, sed quia consequuntur magni dolores eos quira.</p>
<div class="btn btn-green" style="left:616px;top:1086px;width:148px;height:37px">LEARN MORE
  <span class="arrow"><svg width="12" height="10" viewBox="0 0 12 10"><path d="M1 5h9M6 1l4 4-4 4" stroke="var(--green)" stroke-width="1.8" fill="none"/></svg></span>
</div>

<!-- Services -->
<section class="abs services"></section>
<h2 class="abs heading center-text" style="top:1294px;font-size:45px;color:#333;font-weight:500">Our Services</h2>
<p class="abs center-text" style="top:1360px;font-size:14.5px;line-height:26px;color:#444">Kaperspiciatis unde omnis iste natus error sit voluptatem accusantium doloremque laudantium, totam<br>rem aperiam, eaque ipsa quae ab illo inventore</p>
<p class="abs center-text" style="top:1425px;font-size:14.5px;color:#444">Saeritatis et quasi architecto beatae vitae dicta sunt explicabo. Nemo enim ipsam voluptatem quia voluptas sit aspe</p>

<svg class="abs" style="left:0;top:0" width="1200" height="2050" aria-label="Service wheel">
  <g stroke="var(--green)" stroke-width="1.2" fill="none">
    <polyline points="349,1525 458,1525 458,1560"/>
    <line x1="349" y1="1653" x2="430" y2="1653"/>
    <polyline points="349,1779 458,1779 458,1745"/>
    <polyline points="849,1525 741,1525 741,1560"/>
    <line x1="849" y1="1653" x2="770" y2="1653"/>
    <polyline points="849,1779 741,1779 741,1745"/>
    <line x1="600" y1="1824" x2="600" y2="1858"/>
  </g>
  <g fill="var(--green)">
    <circle cx="349" cy="1525" r="3.5"/><circle cx="349" cy="1653" r="3.5"/><circle cx="349" cy="1779" r="3.5"/>
    <circle cx="849" cy="1525" r="3.5"/><circle cx="849" cy="1653" r="3.5"/><circle cx="849" cy="1779" r="3.5"/>
    <circle cx="600" cy="1860" r="3.5"/>
  </g>
  <g transform="translate(600,1653)" stroke="#fff" stroke-width="4">
    <path d="M0,-171 A171,171 0 0 1 120.9,-120.9 L65.05,-65.05 A92,92 0 0 0 0,-92 Z" fill="#3e9c37"/>
    <path d="M120.9,-120.9 A171,171 0 0 1 171,0 L92,0 A92,92 0 0 0 65.05,-65.05 Z" fill="#2a8a31"/>
    <path d="M171,0 A171,171 0 0 1 120.9,120.9 L65.05,65.05 A92,92 0 0 0 92,0 Z" fill="#1c7a2b"/>
    <path d="M120.9,120.9 A171,171 0 0 1 0,171 L0,92 A92,92 0 0 0 65.05,65.05 Z" fill="#2c8a34"/>
    <path d="M0,171 A171,171 0 0 1 -120.9,120.9 L-65.05,65.05 A92,92 0 0 0 0,92 Z" fill="#55a83a"/>
    <path d="M-120.9,120.9 A171,171 0 0 1 -171,0 L-92,0 A92,92 0 0 0 -65.05,65.05 Z" fill="#7cc242"/>
    <path d="M-171,0 A171,171 0 0 1 -120.9,-120.9 L-65.05,-65.05 A92,92 0 0 0 -92,0 Z" fill="#6ab73e"/>
    <path d="M-120.9,-120.9 A171,171 0 0 1 0,-171 L0,-92 A92,92 0 0 0 -65.05,-65.05 Z" fill="#58aa3c"/>
    <circle r="88" fill="#fff" stroke="none"/>
    <g fill="none" stroke="#fff" stroke-width="2">
      <circle cx="50.1" cy="-121" r="15"/><circle cx="121" cy="-50.1" r="15"/>
      <circle cx="121" cy="50.1" r="15"/><circle cx="50.1" cy="121" r="15"/>
      <circle cx="-50.1" cy="121" r="15"/><circle cx="-121" cy="50.1" r="15"/>
      <circle cx="-121" cy="-50.1" r="15"/><circle cx="-50.1" cy="-121" r="15"/>
    </g>
  </g>
</svg>
<div class="abs svc-label" style="left:120px;width:208px;text-align:right;top:1515px">Acusantium Foloremq</div>
<div class="abs svc-label" style="left:110px;width:218px;text-align:right;top:1643px">Consectetur Adipiscing</div>
<div class="abs svc-label" style="left:110px;width:215px;text-align:right;top:1769px">Oaudantium Sotamrem</div>
<div class="abs svc-label" style="left:865px;top:1515px">Minima Saeniam</div>
<div class="abs svc-label" style="left:865px;top:1643px">Seprehend Eritqune</div>
<div class="abs svc-label" style="left:865px;top:1769px">Kaiusmodi Uempora</div>
<div class="abs svc-label center-text" style="top:1869px">Sacasionally Raircumsta</div>
<div class="btn btn-green" style="left:526px;top:1928px;width:148px;height:36px">LEARN MORE
  <span class="arrow"><svg width="12" height="10" viewBox="0 0 12 10"><path d="M1 5h9M6 1l4 4-4 4" stroke="var(--green)" stroke-width="1.8" fill="none"/></svg></span>
</div>

<!-- Sustainable -->
<section class="abs sustain">
  <div class="abs" role="img" aria-label="Worker tending potted plants in a greenhouse while taking notes" style="left:0;top:0;width:1200px;height:492px;clip-path:polygon(816px 0,1200px 0,1200px 492px,640px 492px);background:linear-gradient(135deg,#b8b7ab 0%,#8f8b72 40%,#5c6a3a 70%,#3f4a2a 100%)"></div>
</section>
<h2 class="abs heading" style="left:108px;top:2118px;font-size:44px;color:var(--white)">Sustainable</h2>
<p class="abs" style="left:115px;top:2179px;width:510px;font-size:14.5px;line-height:25.6px;color:var(--white)">Kaospiciatis unde omnis iste natus error sit voluptatem accusantium doloremque laudantium, totam rem aperiam, eaque ipsa quae ab illo inventore veritatis.</p>
<p class="abs" style="left:115px;top:2262px;width:500px;font-size:14.5px;line-height:25.6px;color:var(--white)">Oaerspiciatis unde omnis iste natus error sit volupt atem accusantium doloremque laudant ium, totam rem aperiam, eaque ipsa quae ab illo inventore veritatis et quasi architecto beata seevitae dicta sunt explicabo. Nemo enimipsam voluptatem quia voluptasit asedula. audant ium, totam rem aperiam, eaque ipsa quae ab illo inventore veritatis et quasi.</p>
<div class="btn btn-white" style="left:115px;top:2428px;width:149px;height:37px">LEARN MORE
  <span class="arrow"><svg width="12" height="10" viewBox="0 0 12 10"><path d="M1 5h9M6 1l4 4-4 4" stroke="#666" stroke-width="1.5" fill="none"/></svg></span>
</div>

<!-- Articles -->
<section class="abs" style="left:0;top:2542px;width:1200px;height:627px;background:var(--panel)"></section>
<h2 class="abs heading center-text" style="top:2608px;font-size:45px;color:#333;font-weight:500">Our Articles</h2>

<article class="abs card" style="left:110px">
  <div class="photo" role="img" aria-label="Stainless steel juice bottling line in a factory" style="background:linear-gradient(160deg,#dfe3e6,#9aa3a8 50%,#c8a05a 85%)"></div>
  <div class="meta">March, 2022 I 2 Comments</div>
  <h3 class="title">Saerspiciatis unde omnisiste<br>natus error sitvoluptatem</h3>
  <p class="text">Perspiciatis unde omnis iste natus error sit voluptatem accusantium doloremquese</p>
  <div class="link">View Full Articles <svg width="18" height="10" viewBox="0 0 18 10"><path d="M0 5h16M12 1l4 4-4 4" stroke="var(--green)" stroke-width="1.6" fill="none"/></svg></div>
</article>
<article class="abs card" style="left:444px">
  <div class="photo" role="img" aria-label="Garlic bulbs moving along a blue processing conveyor" style="background:linear-gradient(180deg,#7b8790,#2f5f9c 55%,#e8e3d8 80%,#3a6fb0)"></div>
  <div class="meta">March, 2022 I 2 Comments</div>
  <h3 class="title">Saerspiciatis unde omnisiste<br>natus error sitvoluptatem</h3>
  <p class="text">Perspiciatis unde omnis iste natus error sit voluptatem accusantium doloremquese</p>
  <div class="link">View Full Articles <svg width="18" height="10" viewBox="0 0 18 10"><path d="M0 5h16M12 1l4 4-4 4" stroke="var(--green)" stroke-width="1.6" fill="none"/></svg></div>
</article>
<article class="abs card" style="left:775px">
  <div class="photo" role="img" aria-label="Inspector in white coveralls checking apples on a sorting line" style="background:linear-gradient(180deg,#d8dcdd,#9ea6aa 45%,#c9603a 75%,#3b6aa8)"></div>
  <div class="meta">March, 2022 I 2 Comments</div>
  <h3 class="title">Saerspiciatis unde omnisiste<br>natus error sitvoluptatem</h3>
  <p class="text">Perspiciatis unde omnis iste natus error sit voluptatem accusantium doloremquese</p>
  <div class="link">View Full Articles <svg width="18" height="10" viewBox="0 0 18 10"><path d="M0 5h16M12 1l4 4-4 4" stroke="var(--green)" stroke-width="1.6" fill="none"/></svg></div>
</article>

<!-- Contact -->
<section class="abs contact"></section>
<div class="brand-dot" style="left:112px;top:3256px;width:40px;height:40px"></div>
<div class="abs" style="left:170px;top:3258px;width:1px;height:52px;background:#444"></div>
<div class="abs brand" style="left:184px;top:3262px;font-size:29px;color:#333">Varnelux7</div>
<div class="abs" style="left:187px;top:3300px;font-size:18px;color:#333;white-space:nowrap">Results Matter. Work Hard.</div>
<h2 class="abs heading" style="left:110px;top:3355px;font-size:33px;line-height:45px;color:#1e1e1e;font-weight:500;white-space:nowrap">Get In Touch With<br>Us Varnelux7</h2>
<p class="abs" style="left:112px;top:3471px;font-size:19px;color:#222;white-space:nowrap">Reach out to discuss your needs.</p>
<p class="abs" style="left:112px;top:3508px;font-size:19px;color:#222;white-space:nowrap">hello@varnelux7-mail.com</p>

<div class="abs field-label" style="left:497px;top:3251px">YOUR NAME</div>
<div class="abs field" style="left:497px;top:3270px;width:256px;height:38px">Jane Sample</div>
<div class="abs field-label" style="left:783px;top:3251px">COMPANY</div>
<div class="abs field" style="left:783px;top:3270px;width:256px;height:38px">jane.sample@mailbox.com</div>
<div class="abs field-label" style="left:497px;top:3331px">EMAIL ADDRESS</div>
<div class="abs field" style="left:497px;top:3351px;width:256px;height:38px">jane.sample@mailbox.com</div>
<div class="abs field-label" style="left:783px;top:3331px">PHONE</div>
<div class="abs field" style="left:783px;top:3351px;width:256px;height:38px">555 010 2299</div>
<div class="abs field-label" style="left:497px;top:3409px">MESSAGE</div>
<div class="abs field" style="left:497px;top:3427px;width:541px;height:99px;align-items:flex-start;padding-top:10px">Hi, do you have a momment to talk abo....</div>
<div class="btn btn-green" style="left:497px;top:3537px;width:150px;height:36px">SUBMIT
  <span class="arrow"><svg width="12" height="10" viewBox="0 0 12 10"><path d="M1 5h9M6 1l4 4-4 4" stroke="var(--green)" stroke-width="1.8" fill="none"/></svg></span>
</div>

<!-- Footer -->
<footer class="abs footer"></footer>
<div class="brand-dot" style="left:112px;top:3793px;width:34px;height:34px"></div>
<div class="abs" style="left:158px;top:3795px;width:1px;height:44px;background:#888"></div>
<div class="abs brand" style="left:168px;top:3797px;font-size:24px;color:var(--white)">Varnelux7</div>
<div class="abs" style="left:172px;top:3830px;font-size:15px;color:var(--white);white-space:nowrap">Results Matter. Work Hard.</div>

<div class="abs foot-head" style="left:423px">Quick Links</div>
<ul class="abs foot-list" style="left:423px"><li>Home</li><li>About Us</li><li>Our Services</li><li>Case Study</li><li>Our Blog</li><li>Contact Us</li></ul>
<div class="abs foot-head" style="left:600px">Support</div>
<ul class="abs foot-list" style="left:600px"><li>Team</li><li>About Us</li><li>Careers</li><li>Our Values</li></ul>
<div class="abs foot-head" style="left:744px">Links</div>
<ul class="abs foot-list" style="left:744px"><li>Copyright</li><li>Legal</li><li>Privacy</li><li>Accessibility</li><li>Sitemap</li></ul>
<div class="abs foot-head" style="left:892px">Contact Us</div>

<svg class="abs" style="left:892px;top:3786px" width="16" height="22" viewBox="0 0 16 22"><path d="M8 0a8 8 0 0 0-8 8c0 6 8 14 8 14s8-8 8-14a8 8 0 0 0-8-8zm0 11a3 3 0 1 1 0-6 3 3 0 0 1 0 6z" fill="var(--green)"/></svg>
<div class="abs foot-small" style="left:918px;top:3780px">Address</div>
<div class="abs foot-text" style="left:918px;top:3794px;line-height:19px">88 Orchard Row, Fieldmont,<br>USA</div>
<svg class="abs" style="left:892px;top:3846px" width="16" height="16" viewBox="0 0 24 24"><path d="M6.6 10.8c1.4 2.8 3.8 5.1 6.6 6.6l2.2-2.2c.3-.3.7-.4 1-.2 1.1.4 2.3.6 3.6.6.6 0 1 .4 1 1V20c0 .6-.4 1-1 1C10.6 21 3 13.4 3 4c0-.6.4-1 1-1h3.5c.6 0 1 .4 1 1 0 1.3.2 2.5.6 3.6.1.3 0 .7-.2 1z" fill="var(--green)"/></svg>
<div class="abs foot-small" style="left:918px;top:3841px">Phone</div>
<div class="abs foot-text" style="left:918px;top:3855px">+1 (555) 010 4420</div>
<svg class="abs" style="left:892px;top:3890px" width="16" height="12" viewBox="0 0 22 16"><rect x="1" y="1" width="20" height="14" fill="var(--green)"/><path d="M1 1l10 8 10-8" stroke="#000" stroke-width="1.6" fill="none"/></svg>
<div class="abs foot-small" style="left:918px;top:3884px">Mail</div>
<div class="abs foot-text" style="left:918px;top:3897px">hello@varnelux7-mail.com</div>

<div class="abs" style="left:110px;top:3946px;width:977px;height:1px;background:#2a5a2a"></div>
<div class="abs foot-text" style="left:110px;top:3971px;font-size:13px">Copyright © 2022 | All Rights Reserved</div>
<div class="abs foot-legal" style="left:808px;top:3972px">TERMS &amp; CONDITIONS</div>
<div class="abs" style="left:962px;top:3968px;width:1px;height:18px;background:var(--green)"></div>
<div class="abs foot-legal" style="left:988px;top:3972px">PRIVACY POLICY</div>
<div class="abs" style="left:1122px;top:3922px;width:42px;height:42px;border-radius:50%;background:#0f9a2a;display:flex;align-items:center;justify-content:center">
  <svg width="12" height="8" viewBox="0 0 12 8"><path d="M1 7l5-5 5 5" stroke="#fff" stroke-width="1.8" fill="none"/></svg>
</div>

</body>
</html>
```